Cosmetic oil label design

We need a label for a cosmetic oganic Argan Oil. The oil is organic imported from Morocco, cold pressed without any preservatives. The lable is for our round 30ml Airless Bottle with clear body Matte Gold Cap, Shiny Gold Collar. We want to communicate that our product is organic natural and works for all beauty needs. We want the emphasis on the words No preservatives, additives or perfumes
We have attached a picture of the bottle and our compnay's logo.

the bottle demensions are Width/Front: 33.0mm
Length/Depth: 33.0mm
Height: 115.0mm
Lable demensions: Lenght 4inch, width 1.75inch.

let us know if you need any other information, cheers!
Updates

Target Market(s)

Our target customer is mainly women 16-70, and also men or anyone looking to have healthy skin and hair using natural products

Industry/Entity Type

Product

Requirements
Must have
• Front side must have:
- attached logo
-words: Authentic Moroccan Argan Oil, No preservatives, additives or perfumes,
L’Huile d’Argan, Produit du Maroc, Imported from Morocco, 30ml

Back side
-Ingredients: 100% Pure Argania Spinosa (Argan Oil)
-Directions: Message into skin, hair or desired area until completely absorbed
-Manufactured for and distributed by Luvera Imports
418 W 97th street New York , NY 10027
Nice to have
• Would be nice if we can fit the following information in the back of the label

Rich in vitamin E and essential fatty acids,Argan oil has several benefits. It Hydrates and nourishes skin and hair. Can be used for treating dry skin, split ends softening cuticles. It works for all types of skin.

```html
<!DOCTYPE html>
<html lang="en">
<head>
<meta charset="utf-8">
<title>Soleva Moroccan Argan Oil – 30ml Label</title>
<link rel="stylesheet" href="https://fonts.googleapis.com/css2?family=Cinzel:wght@400&family=Gentium+Book+Plus&family=Roboto+Condensed:wght@700&display=swap">
<style>
  :root {
    --ink-dark: #1f1710;
    --band-dark: #231a12;
    --bar-dark: #211b15;
    --gold: #e9b95e;
    --gold-soft: #e6b862;
    --olive: #8b7e36;
    --bronze: #3b2b17;
    --seal-ring: #6b5638;
  }
  * { margin: 0; padding: 0; box-sizing: border-box; }
  html, body { width: 1200px; height: 2743px; overflow: hidden; background: var(--band-dark); }
  .label {
    position: relative;
    width: 1200px;
    height: 2743px;
    overflow: hidden;
    background: linear-gradient(180deg,
      var(--bronze) 0%,
      var(--bronze) 30%,
      #7a5a2c 38%,
      var(--gold) 54%,
      #c9a262 66%,
      #6a5234 84%,
      #2d241a 96%);
  }
  .top-band {
    position: absolute;
    left: 0; top: 0;
    width: 1200px; height: 834px;
    background: var(--band-dark);
  }
  .top-band-curve {
    position: absolute;
    left: 25px; top: 628px;
    width: 1150px; height: 412px;
    border-radius: 50%;
    background: var(--band-dark);
  }
  .volume {
    position: absolute;
    right: 34px; top: 42px;
    font-family: "Gentium Book Plus", serif;
    font-size: 66px;
    color: var(--gold-soft);
  }
  .brand-name {
    position: absolute;
    left: 0; width: 1200px; top: 660px;
    text-align: center;
    font-family: "Cinzel", serif;
    font-weight: 400;
    font-size: 190px;
    line-height: 1;
    color: var(--olive);
  }
  .product-title {
    position: absolute;
    left: 0; width: 1200px; top: 1370px;
    font-family: "Cinzel", serif;
    font-weight: 400;
    color: var(--ink-dark);
    font-size: 150px;
    line-height: 178px;
    text-align: center;
  }
  .product-title span { display: block; }
  .product-title .line-oil { padding-right: 60px; }
  .free-from-seal {
    position: absolute;
    left: 578px; top: 2054px;
    width: 600px; height: 600px;
  }
  .seal-ring-text {
    font-family: "Roboto Condensed", sans-serif;
    font-weight: 700;
    font-size: 46px;
    fill: var(--gold-soft);
  }
  .seal-center-text {
    font-family: "Roboto Condensed", sans-serif;
    font-weight: 700;
    font-size: 74px;
    fill: var(--ink-dark);
  }
  .origin-bar {
    position: absolute;
    left: 0; top: 2629px;
    width: 1200px; height: 114px;
    background: var(--bar-dark);
    display: flex;
    align-items: center;
    justify-content: center;
    font-family: "Gentium Book Plus", serif;
    font-size: 68px;
    color: var(--gold-soft);
  }
</style>
</head>
<body>
<main class="label">
  <div class="top-band"></div>
  <div class="top-band-curve"></div>

  <div class="volume">30ml</div>
  <div class="brand-name">Soleva</div>

  <h1 class="product-title">
    <span class="line-moroccan">MOROCCAN</span>
    <span class="line-argan">ARGAN</span>
    <span class="line-oil">OIL</span>
  </h1>

  <svg class="free-from-seal" viewBox="0 0 600 600" aria-label="Free from preservatives, perfumes, additives">
    <g fill="var(--band-dark)">
      <rect x="92" y="92" width="416" height="416" transform="rotate(0 300 300)"/>
      <rect x="92" y="92" width="416" height="416" transform="rotate(11.25 300 300)"/>
      <rect x="92" y="92" width="416" height="416" transform="rotate(22.5 300 300)"/>
      <rect x="92" y="92" width="416" height="416" transform="rotate(33.75 300 300)"/>
      <rect x="92" y="92" width="416" height="416" transform="rotate(45 300 300)"/>
      <rect x="92" y="92" width="416" height="416" transform="rotate(56.25 300 300)"/>
      <rect x="92" y="92" width="416" height="416" transform="rotate(67.5 300 300)"/>
      <rect x="92" y="92" width="416" height="416" transform="rotate(78.75 300 300)"/>
    </g>
    <circle cx="300" cy="300" r="250" fill="none" stroke="var(--seal-ring)" stroke-width="10"/>
    <circle cx="300" cy="300" r="132" fill="none" stroke="var(--seal-ring)" stroke-width="8"/>
    <circle cx="300" cy="300" r="126" fill="var(--gold-soft)"/>
    <defs>
      <path id="seal-ring-path" d="M112,300 a188,188 0 1,1 376,0 a188,188 0 1,1 -376,0"/>
    </defs>
    <g transform="rotate(-48 300 300)">
      <text class="seal-ring-text" dy="16">
        <textPath href="#seal-ring-path" textLength="1160" lengthAdjust="spacing">PRESERVATIVES * PERFUMES * ADDITIVES * </textPath>
      </text>
    </g>
    <text class="seal-center-text" x="300" y="292" text-anchor="middle">FREE</text>
    <text class="seal-center-text" x="300" y="364" text-anchor="middle">FROM</text>
  </svg>

  <footer class="origin-bar">L’Huile d’Argan, Produit du Maroc.</footer>
</main>
</body>
</html>
```